Corvanta Solutions Sales Materials & Look

I am looking for an impactful design to a sales/presentation folder.

On the top of the folder I want the power quotes
Pure Nutrition From Phytoplankton
The World's Original Whole Food
The Best Results In Natural Health History

*picture of powder
Corvanta logo.

The colors and font on the corvanta logo are important to keep in tact even for the power quotes.
I'll leave it up to you how you want to stylize it.

On the back on the bottom (subtle) I want the following
Logo
Unit #5 - 418 Harlow Avenue
Moncton, New Brunswick
Canada
(506) 555 0174
Plus any other styling you want to consider.

We sell marine phytoplankton powder to other businesses. Marine Phytoplankton is the original vegetable on the planet. It's positioned as a natural medicine for chrohn's and colitis, and fibromyalgia.

I have added the business card design. Please add the following information
Martin Greaves - Founder - CEO
email - mkgreaves@corvanta.example
Phone - (506) 555 0192
Corvanta Solutions Inc
Unit #5 - 418 Harlow Avenue
Moncton, New Brunswick
E1A 4K7
Canada

```html
<!DOCTYPE html>
<html lang="en">
<head>
<meta charset="utf-8">
<title>Corvanta Solutions – Business Card</title>
<link rel="stylesheet" href="https://fonts.googleapis.com/css2?family=Montserrat:wght@300;400;700;800&display=swap">
<style>
  :root {
    --bg: #484848;
    --card: #141414;
    --edge: #27a9e1;
    --brand-blue: #27a9e1;
    --brand-green: #8cc63f;
    --ink: #f2f2f2;
    --emboss: #1e1e1e;
  }
  * { box-sizing: border-box; margin: 0; padding: 0; }
  html, body { width: 1200px; height: 801px; overflow: hidden; }
  body {
    background: var(--bg);
    font-family: "Montserrat", sans-serif;
    display: flex;
    align-items: center;
    justify-content: center;
    gap: 40px;
  }
  .card {
    width: 540px;
    height: 309px;
    background: var(--card);
    border-radius: 18px;
    border-bottom: 4px solid var(--edge);
    border-right: 3px solid var(--edge);
    position: relative;
    overflow: hidden;
  }
  /* Front */
  .card-front { display: flex; align-items: center; }
  .brand {
    width: 240px;
    display: flex;
    align-items: center;
    justify-content: center;
    gap: 10px;
  }
  .brand-dot {
    width: 18px; height: 18px;
    border-radius: 50%;
    background: var(--brand-blue);
  }
  .brand-name {
    font-weight: 800;
    font-size: 34px;
    color: var(--brand-blue);
    letter-spacing: -0.5px;
  }
  .divider {
    width: 1.5px;
    height: 190px;
    background: var(--edge);
  }
  .contact {
    padding-left: 26px;
    color: var(--ink);
    font-weight: 300;
    font-size: 12.5px;
    line-height: 1.45;
  }
  .person-name {
    font-weight: 800;
    font-size: 22px;
    color: var(--brand-blue);
    line-height: 1.1;
  }
  .person-title { font-size: 13.5px; margin-bottom: 12px; }
  .contact-line { display: flex; align-items: center; gap: 7px; }
  .contact-line svg { width: 11px; height: 11px; fill: var(--brand-blue); flex: none; }
  .company {
    margin-top: 12px;
    font-weight: 700;
    color: var(--brand-blue);
    font-size: 13px;
  }
  /* Back */
  .card-back {
    display: flex;
    align-items: center;
    justify-content: center;
  }
  .emboss-name {
    font-weight: 800;
    font-size: 86px;
    color: var(--emboss);
    letter-spacing: -1px;
  }
</style>
</head>
<body>
  <section class="card card-front">
    <div class="brand">
      <span class="brand-dot"></span>
      <span class="brand-name">Corvanta</span>
    </div>
    <div class="divider"></div>
    <div class="contact">
      <p class="person-name">Martin Greaves</p>
      <p class="person-title">Founder - CEO</p>
      <p class="contact-line">
        <svg viewBox="0 0 24 24" aria-hidden="true"><path d="M6.6 10.8a15 15 0 0 0 6.6 6.6l2.2-2.2c.3-.3.7-.4 1-.2 1.1.4 2.3.6 3.6.6.6 0 1 .4 1 1V20c0 .6-.4 1-1 1C10.6 21 3 13.4 3 4c0-.6.4-1 1-1h3.5c.6 0 1 .4 1 1 0 1.3.2 2.5.6 3.6.1.3 0 .7-.2 1z"/></svg>
        (506) 555 0192
      </p>
      <p class="contact-line">
        <svg viewBox="0 0 24 24" aria-hidden="true"><path d="M2 5h20v14H2z M2 5l10 8 10-8" /></svg>
        mkgreaves@corvanta.example
      </p>
      <p class="company">Corvanta Solutions Inc</p>
      <p>Unit #5 - 418 Harlow Avenue</p>
      <p>Moncton, New Brunswick</p>
      <p>E1A 4K7 Canada</p>
    </div>
  </section>

  <section class="card card-back">
    <span class="emboss-name">Corvanta</span>
  </section>
</body>
</html>
```